Web Design Project

New website for Aged Care business.

Easy buttons to

1.book appointment

2.request a callback

3.view services

think elderly people using it, or family members

we like the colours of 'tidewell' website

and the middle image and call to action buttons of the rons edging website.

we'd like a rotating image similar to the rons edging but bigger size.

http://www.tidewell.org.au/

http://www.ronsedging.net/

Reason: need to have a meeting with our staff to decide - i'm overseas..

Target Market(s)

elderly people and families of elderly people with enough money to pay for the services offered.

Industry/Entity Type

Business

Requirements
Must have
• contemporary and clean design

```html
<!DOCTYPE html>
<html lang="en">
<head>
<meta charset="utf-8">
<title>Harbourne Care</title>
<link rel="stylesheet" href="https://fonts.googleapis.com/css2?family=Noto+Sans:wght@400;700&family=Tinos:wght@400;700&display=swap">
<style>
  :root {
    --sky: #8fcfe7;
    --paper: #ffffff;
    --brand: #1a9ad6;
    --brand-deep: #0a6f9c;
    --nav-top: #11a6d6;
    --nav-bottom: #06729f;
    --ink: #4a4a4a;
    --ink-dark: #2f2f2f;
    --rule: #e2e2e2;
    --field: #f4f4f4;
    --field-edge: #cfcfcf;
    --leaf: #8cc63f;
    --leaf-deep: #5f9a1e;
    --news-link: #1a9ad6;
    --news-date: #0a5f86;
  }
  * { box-sizing: border-box; margin: 0; padding: 0; }
  html, body { width: 1097px; height: 1200px; overflow: hidden; }
  body {
    background: var(--sky);
    font-family: "Noto Sans", sans-serif;
    color: var(--ink);
  }
  .stage {
    position: relative;
    width: 1024px;
    height: 1120px;
    transform: scale(1.0713);
    transform-origin: 0 0;
  }
  .page {
    position: absolute;
    left: 54px; top: 10px;
    width: 922px; height: 1024px;
    background: var(--paper);
    box-shadow: 0 1px 4px rgba(0,0,0,.25);
    border-radius: 2px;
  }
  .abs { position: absolute; }

  .brand-name {
    left: 31px; top: 28px;
    font-size: 23px; font-weight: 700;
    color: var(--brand);
    letter-spacing: -0.3px;
  }

  .main-nav {
    left: 31px; top: 78px;
    width: 853px; height: 43px;
    background: linear-gradient(var(--nav-top), var(--nav-bottom));
    border-radius: 3px;
    display: flex; align-items: center;
  }
  .main-nav a {
    color: #fff; text-decoration: none;
    font-size: 13px;
    height: 43px; line-height: 43px;
    padding: 0 10px;
    border-right: 1px solid rgba(255,255,255,.22);
  }
  .main-nav a:first-child { padding-left: 21px; }
  .main-nav a:last-of-type { border-right: 0; padding-left: 16px; }
  .search-field {
    position: absolute; left: 599px; top: 10px;
    width: 183px; height: 27px;
    background: #0b6890;
    border: 1px solid #05506f;
    border-radius: 3px 0 0 3px;
  }
  .search-btn {
    position: absolute; left: 783px; top: 11px;
    width: 62px; height: 25px;
    background: linear-gradient(#3cc1e4, #1596c2);
    color: #fff; font-size: 13px;
    line-height: 25px; text-align: center;
    border-radius: 0 3px 3px 0;
  }

  .hero {
    left: 31px; top: 131px;
    width: 853px; height: 270px;
    border: 1px solid #d6d6d6;
    border-radius: 3px;
    box-shadow: 0 1px 3px rgba(0,0,0,.12);
    padding: 5px;
  }
  .hero-image {
    width: 841px; height: 258px;
    background: linear-gradient(100deg, #b9c4b0 0%, #e8ece9 30%, #c7cdd3 55%, #ece9e2 80%, #9c8a76 100%);
    position: relative;
  }
  .hero-caption {
    position: absolute; right: 10px; bottom: 10px;
    font-size: 26px; font-weight: 700;
    color: var(--brand-deep);
  }

  .section-title {
    font-family: "Tinos", serif;
    color: var(--brand);
    font-weight: 400;
  }
  .about-title { left: 37px; top: 420px; font-size: 32px; }
  .about-rule { left: 31px; top: 462px; width: 518px; height: 1px; background: var(--rule); }
  .about-copy {
    left: 38px; top: 480px; width: 514px;
    font-size: 12.6px; line-height: 20.4px;
    color: var(--ink);
  }
  .about-copy p + p { margin-top: 20px; }

  .offer-icon { left: 586px; top: 429px; }
  .offer-title { left: 615px; top: 421px; font-size: 30px; }
  .offer-rule { left: 584px; top: 462px; width: 300px; height: 1px; background: var(--rule); }
  .offer-list {
    left: 586px; top: 480px; width: 300px;
    list-style: none;
    font-size: 12.6px; line-height: 20.4px;
    color: var(--ink-dark);
  }
  .offer-list li { position: relative; padding-left: 18px; margin-bottom: 2px; }
  .offer-list svg { position: absolute; left: 0; top: 5px; }

  .panel-title {
    font-size: 16px; color: var(--brand-deep); font-weight: 400;
  }
  .booking-title { left: 41px; top: 712px; }
  .field {
    left: 38px; width: 278px; height: 29px;
    background: var(--field);
    border: 1px solid var(--field-edge);
    border-radius: 2px;
    box-shadow: inset 0 1px 2px rgba(0,0,0,.08);
    font-size: 12.5px; color: #222;
    line-height: 27px; padding-left: 10px;
  }
  .field .hint { color: #b5b5b5; margin-left: 6px; }
  .btn {
    height: 30px; line-height: 30px; text-align: center;
    font-size: 13px; border-radius: 2px;
  }
  .btn-later { left: 37px; top: 932px; width: 139px; background: linear-gradient(#e6e6e6, #c7c7c7); color: #333; border: 1px solid #bdbdbd; }
  .btn-now { left: 181px; top: 932px; width: 140px; background: linear-gradient(#4fc2e8, #2a9fcc); color: #fff; border: 1px solid #2492bd; }

  .callback-card {
    left: 354px; top: 730px; width: 183px; height: 98px;
    border: 1px solid #9a9a9a; border-radius: 8px;
    background: linear-gradient(#ffffff, #ececec);
    overflow: hidden;
    box-shadow: 0 1px 2px rgba(0,0,0,.2);
  }
  .callback-text {
    position: absolute; left: 8px; top: 8px;
    font-family: "Tinos", serif; font-weight: 700;
    font-size: 22px; line-height: 26px; color: #5a5a5a;
  }
  .callback-photo {
    position: absolute; right: 0; top: 0; width: 88px; height: 98px;
    background: linear-gradient(#e9dfd8, #cdbfb6);
  }
  .go-btn {
    height: 22px; width: 83px;
    background: linear-gradient(#9ad04a, var(--leaf-deep));
    border: 1px solid #4e8416;
    border-radius: 4px;
    color: #fff; font-size: 12.5px;
    line-height: 20px; padding-left: 5px;
    display: flex; align-items: center; gap: 3px;
  }
  .callback-card .go-btn { position: absolute; left: 10px; top: 67px; }

  .newsletter-card {
    left: 354px; top: 848px; width: 186px; height: 108px;
    border: 1px solid #8f8f8f; border-radius: 8px;
    background: #fff;
  }
  .newsletter-card .label { position: absolute; left: 15px; top: 11px; font-size: 13px; color: #222; }
  .newsletter-card .pill {
    position: absolute; left: 10px; top: 40px; width: 163px; height: 22px;
    border: 1px solid #cfcfcf; border-radius: 11px;
    background: var(--field);
    font-size: 12.5px; line-height: 20px; padding-left: 17px; color: #222;
  }
  .newsletter-card .go-btn { position: absolute; left: 10px; top: 76px; }

  .news-title { left: 589px; top: 712px; }
  .news-list { left: 588px; top: 743px; width: 295px; list-style: none; font-size: 12.6px; line-height: 20px; color: var(--ink-dark); }
  .news-list li { margin-bottom: 18px; }
  .news-list li:nth-child(3) { padding-left: 4px; }
  .news-list a { color: var(--news-link); }
  .news-list .date { color: var(--news-date); font-size: 12.5px; }
  .news-list .date small { font-size: 11px; }

  .site-footer {
    left: 64px; top: 1046px;
    font-size: 12.6px; line-height: 21px; color: #2a2a2a;
  }
</style>
</head>
<body>
<div class="stage">
  <div class="page">
    <div class="abs brand-name">Harbourne Care</div>

    <nav class="abs main-nav">
      <a href="#">Care and Support</a>
      <a href="#">Retirement Living</a>
      <a href="#">Our Locations</a>
      <a href="#">Our Community</a>
      <a href="#">About Us</a>
      <div class="search-field"></div>
      <div class="search-btn">Search</div>
    </nav>

    <div class="abs hero">
      <div class="hero-image" role="img" aria-label="Rotating banner photo: a smiling carer standing beside an elderly man in a hat, outdoors under trees">
        <span class="hero-caption">Harbourne Care</span>
      </div>
    </div>

    <h2 class="abs section-title about-title">about us</h2>
    <div class="abs about-rule"></div>
    <div class="abs about-copy">
      <p>Lorem ipsum dolor sit amet, consectetur adipisicing elit, sed do eiusmod tempor incididunt ut labore et dolore magna aliqua. Ut enim ad minim veniam, quis nostrud exercitation ullamco laboris nisi ut aliquip ex ea commodo consequat. Duis aute irure dolor in reprehenderit in voluptate velit esse cillum dolore eu fugiat nulla pariatur. Excepteur sint occaecat cupidatat non proident, sunt in culpa qui officia deserunt mollit anim id est laborum.</p>
      <p>Lorem ipsum dolor sit amet, consectetur adipisicing elit, sed do eiusmod tempor incididunt ut labore et dolore magna aliqua. Ut enim ad minim veniam, quis nostrud exercitation ullamco laboris nisi ut aliquip.</p>
    </div>

    <svg class="abs offer-icon" width="20" height="20" viewBox="0 0 20 20" aria-hidden="true">
      <rect x="0" y="9" width="5" height="11" fill="#4fb7e3"/>
      <rect x="7" y="4" width="5" height="16" fill="#f1b33b"/>
      <rect x="14" y="0" width="5" height="20" fill="#8cc63f"/>
    </svg>
    <h2 class="abs section-title offer-title">What We Offer</h2>
    <div class="abs offer-rule"></div>
    <ul class="abs offer-list">
      <li><svg width="11" height="11" viewBox="0 0 11 11"><path d="M4 0h3v4h4v3H7v4H4V7H0V4h4z" fill="var(--leaf)"/></svg>voluptates repudiandae sint et molestiae non recusandae</li>
      <li><svg width="11" height="11" viewBox="0 0 11 11"><path d="M4 0h3v4h4v3H7v4H4V7H0V4h4z" fill="var(--leaf)"/></svg>Sed ut perspiciatis unde omnis iste natus error sit voluptatem accusantium</li>
      <li><svg width="11" height="11" viewBox="0 0 11 11"><path d="M4 0h3v4h4v3H7v4H4V7H0V4h4z" fill="var(--leaf)"/></svg>qui dolorem ipsum quia dolor sit amet &nbsp;con sectetur, adipisci velit</li>
      <li><svg width="11" height="11" viewBox="0 0 11 11"><path d="M4 0h3v4h4v3H7v4H4V7H0V4h4z" fill="var(--leaf)"/></svg>At vero eos et accusamus et iusto odio</li>
      <li><svg width="11" height="11" viewBox="0 0 11 11"><path d="M4 0h3v4h4v3H7v4H4V7H0V4h4z" fill="var(--leaf)"/></svg>voluptates repudiandae sint et molestiae non recusandae</li>
    </ul>

    <h3 class="abs panel-title booking-title">Book Appointment</h3>
    <div class="abs field" style="top:739px">NAME</div>
    <div class="abs field" style="top:778px">EMAIL ID</div>
    <div class="abs field" style="top:816px">DATE - <span class="hint">DD/MM/YY</span></div>
    <div class="abs field" style="top:855px">TIME -</div>
    <div class="abs field" style="top:893px">MESSAGE</div>
    <div class="abs btn btn-later">BOOK LATER</div>
    <div class="abs btn btn-now">BOOK NOW</div>

    <div class="abs callback-card">
      <div class="callback-text">Request<br>call back</div>
      <div class="callback-photo" role="img" aria-label="Photo of a smiling call centre agent wearing a headset"></div>
      <div class="go-btn">Click here
        <svg width="14" height="10" viewBox="0 0 14 10" aria-hidden="true"><path d="M1 1l4 4-4 4M7 1l4 4-4 4" stroke="#fff" stroke-width="2" fill="none"/></svg>
      </div>
    </div>

    <div class="abs newsletter-card">
      <div class="label">Newsletter Signup</div>
      <div class="pill">email id</div>
      <div class="go-btn">Click here
        <svg width="14" height="10" viewBox="0 0 14 10" aria-hidden="true"><path d="M1 1l4 4-4 4M7 1l4 4-4 4" stroke="#fff" stroke-width="2" fill="none"/></svg>
      </div>
    </div>

    <h3 class="abs panel-title news-title">In The News</h3>
    <ul class="abs news-list">
      <li><a href="#">Lorem ipsum dolor sit amet,</a> consectetur adipisicing elit, sed do eiusmod tempor incididunt ut <span class="date">Posted <small>-22.4.2012</small></span></li>
      <li><a href="#">Lorem ipsum dolor sit amet, consectetur</a> adipisicing elit, sed do eiusmod tempor incididunt ut labore et. <span class="date">Posted <small>-22.4.2012</small></span></li>
      <li><a href="#">Lorem ipsum dolor sit amet, consectetur</a> adipisicing elit, sed do eiusmod tempor incididunt ut labore et. <span class="date">Posted <small>-22.4.2012</small></span></li>
    </ul>
  </div>

  <footer class="abs site-footer">
    © All right Reserved 2012 | Privacy Statement<br>
    Harbourne Care
  </footer>
</div>
</body>
</html>
```